UK young peoples' debating organisation needs flyers for tournament + promotion for major club laun

I need a flyer for the tournament but also sell the after-school clubs on offer.

Needs to be modern, energetic and fun, challenging the traditional idea of debating as simply academic and elitist.

Must appeal to busy headteachers as well as parents and children.

Target Market(s)

Headteachers; children aged 8 - 11 and their parents

Industry/Entity Type

Education

Font styles to use
Serif
Decorative

Colors

Designer to choose colors to be used in the design.

Requirements
Must have
• The Vantor Oratory logo, plus the Brindlecombe Town Council Logo. The text attached on word doc. (writing in brackets and italics are directions, not to be included as text).
• A space theme (rockets? Stars?/ relates to Vantor. Ideas of movement, aspiration, aiming high etc.
Nice to have
Should not have
• anything relating to pure academia and tradition (mortar boards, suits and ties etc); mo

```html
<!DOCTYPE html>
<html lang="en">
<head>
<meta charset="utf-8">
<title>Vantor Oratory – Calling All Primary and Prep Schools</title>
<link rel="stylesheet" href="https://fonts.googleapis.com/css2?family=Questrial&family=Archivo:ital,wght@0,700;1,500;1,800&display=swap">
<style>
  :root {
    --red: #c0202a;
    --orange: #ee8a22;
    --ink: #1f1f1f;
    --brand-ink: #333333;
    --paper-light: #f6f6f6;
    --paper-mid: #d9d9d9;
    --white: #ffffff;
    --badge-blue: #2f5ea8;
  }
  * { margin: 0; padding: 0; box-sizing: border-box; }
  html, body { width: 928px; height: 1200px; overflow: hidden; }
  body { background: var(--white); }
  .flyer {
    position: relative;
    width: 928px;
    height: 1200px;
    overflow: hidden;
    font-family: "Questrial", "Century Gothic", sans-serif;
    color: var(--ink);
  }
  .flyer__backdrop {
    position: absolute; inset: 0;
    background: radial-gradient(ellipse at 50% 45%, var(--paper-light) 0%, #e6e6e6 60%, var(--paper-mid) 100%);
  }
  .flyer__banner {
    position: absolute; left: 0; top: 67px;
    width: 660px; height: 72px;
  }
  .flyer__banner-title {
    position: absolute; left: 25px; top: 82px;
    font-family: "Archivo", "Arial", sans-serif;
    font-weight: 800; font-style: italic;
    font-size: 27px; letter-spacing: -0.8px;
    color: var(--white); white-space: nowrap;
  }
  .flyer__copy {
    position: absolute; left: 50px; top: 176px; width: 828px;
    font-size: 21.5px; line-height: 30.6px; letter-spacing: 0.6px;
  }
  .flyer__copy .line { display: block; white-space: nowrap; text-align: justify; text-align-last: justify; }
  .flyer__copy .line--end { text-align-last: left; }
  .flyer__copy .gap { height: 30.6px; }
  .flyer__callout {
    position: absolute; left: 50px; top: 702px;
    font-family: "Archivo", "Arial", sans-serif;
    font-weight: 700; font-size: 26px; letter-spacing: 0.4px;
    white-space: nowrap;
  }
  .flyer__contact {
    position: absolute; left: 50px; top: 762px;
    font-style: normal;
    font-size: 21.5px; line-height: 30.5px; letter-spacing: 0.8px;
  }
  .brand__dot {
    position: absolute; left: 707px; top: 696px;
    width: 102px; height: 102px; border-radius: 50%;
    background: var(--red);
  }
  .brand__name {
    position: absolute; left: 628px; top: 815px; width: 268px;
    text-align: center;
    font-family: "Archivo", "Arial", sans-serif;
    font-weight: 700; font-size: 29px; color: var(--brand-ink);
    white-space: nowrap;
  }
  .flyer__waves { position: absolute; left: 0; top: 880px; width: 928px; height: 320px; }
  .council-badge {
    position: absolute; left: 376px; top: 948px;
    width: 176px; height: 176px; border-radius: 50%;
    background: var(--white);
    border: 22px solid var(--badge-blue);
  }
  .flyer__tagline {
    position: absolute; left: 0; width: 928px; top: 1130px;
    text-align: center;
    font-family: "Archivo", "Arial", sans-serif;
    font-style: italic; font-weight: 500; font-size: 17.5px;
  }
</style>
</head>
<body>
<main class="flyer">
  <div class="flyer__backdrop" role="img" aria-label="Light grey background with a faint pattern of speech bubbles"></div>

  <svg class="flyer__banner" viewBox="0 0 660 72" aria-hidden="true">
    <polygon points="0,0 660,0 600,72 0,72" fill="var(--orange)"/>
    <polygon points="0,0 645,0 592,60 0,60" fill="var(--red)"/>
  </svg>
  <h1 class="flyer__banner-title">CALLING ALL PRIMARY AND PREP SCHOOLS</h1>

  <section class="flyer__copy">
    <span class="line">We’ve devised a weekly programme to ensure debating becomes a</span>
    <span class="line">truly enriching part of your school’s culture. &nbsp;Clubs are</span>
    <span class="line line--end">progression-based and teach skills explicitly each week.</span>
    <span class="line">They allow control of learning to be in pupils’ hands, using</span>
    <span class="line">specifically-designed debating notebooks and stickers for each child</span>
    <span class="line line--end">to encourage reflection, research and full participation.</span>
    <span class="gap" aria-hidden="true" style="display:block"></span>
    <span class="line">Our programme is fun, challenging and varied. &nbsp;It also upskills teachers</span>
    <span class="line">keen to take their pupils’ debating to the next level. &nbsp;We’re always on</span>
    <span class="line line--end">hand to help online, or in person where possible.</span>
    <span class="line">By the end of the year we’ll ensure we visit you for a day to help you</span>
    <span class="line">embed debating into your curriculum. &nbsp;You can also opt to enter your</span>
    <span class="line">pupils for the Level 1 Debating qualification from the Redmere Speaking</span>
    <span class="line line--end">Board, for which they will be fully prepared.</span>
    <span class="line">We’re committed to access for all, so please contact for pricing options.</span>
    <span class="line">Give your children the skills to speak confidently, think critically and</span>
    <span class="line line--end">expand their horizons.</span>
  </section>

  <p class="flyer__callout">Give your teachers the chance to lead them.</p>

  <address class="flyer__contact">
    Find out more at www.vantororatory.org<br>
    Chirper: vantororatory@vantororatory<br>
    Email info@vantororatory.org
  </address>

  <span class="brand__dot" aria-hidden="true"></span>
  <span class="brand__name">Vantor Oratory</span>

  <svg class="flyer__waves" viewBox="0 0 928 320" preserveAspectRatio="none" aria-hidden="true">
    <defs>
      <linearGradient id="lowerFill" x1="0" y1="0" x2="0" y2="1">
        <stop offset="0" stop-color="#f8f8f8"/>
        <stop offset="1" stop-color="#d4d4d4"/>
      </linearGradient>
    </defs>
    <path d="M0,105 C170,35 420,20 928,55 L928,320 L0,320 Z" fill="var(--red)"/>
    <path d="M0,118 C180,46 430,32 928,62 L928,320 L0,320 Z" fill="var(--orange)"/>
    <path d="M0,152 C200,70 440,52 928,70 L928,320 L0,320 Z" fill="url(#lowerFill)"/>
  </svg>

  <div class="council-badge" role="img" aria-label="Brindlecombe Town Council badge"></div>

  <p class="flyer__tagline">Promoting debating skills for all young people</p>
</main>
</body>
</html>
```